Business Card Design

We are an IT staffing and consulting company providing IT solutions and resources to our clients.

Industry/Entity Type

Business

Contact Information for Business Card

Ravindra Kolluparthi
Vice President

BrimTrail Inc
48260 Hollyfern Market Court, suite 700
Ashburn, VA 20147
Direct: 571-555-0193
Mobile: 571-555-0147
Email: Ravindra@brimtrailinc.example
Fax: 703-555-0162
www.brimtrailinc.example

```html
<!DOCTYPE html>
<html lang="en">
<head>
<meta charset="utf-8">
<title>BrimTrail Inc – Business Card</title>
<link rel="stylesheet" href="https://fonts.googleapis.com/css2?family=Michroma&display=swap">
<style>
  :root {
    --backdrop: #d9dadb;
    --card: #ffffff;
    --ink: #111111;
    --band: #0d0d0d;
    --accent: #c1272d;
    --on-band: #f2f2f2;
    --muted: #bdbdbd;
  }
  * { box-sizing: border-box; margin: 0; padding: 0; }
  html, body {
    width: 1200px; height: 771px; overflow: hidden;
    background: var(--backdrop);
    font-family: "Michroma", sans-serif;
  }
  .stage {
    position: relative; width: 1200px; height: 771px;
    display: flex; gap: 40px; justify-content: center; align-items: center;
  }
  .card {
    position: relative; width: 540px; height: 309px;
    background: var(--card);
    box-shadow: 0 6px 18px rgba(0,0,0,.18);
    overflow: hidden;
  }
  .wordmark {
    position: absolute; display: flex; align-items: center; gap: 12px;
    color: var(--ink); font-size: 34px; letter-spacing: .5px; white-space: nowrap;
  }
  .wordmark__dot {
    width: 22px; height: 22px; border-radius: 50%; background: var(--accent);
  }
  .card--front .wordmark { left: 50%; top: 50%; transform: translate(-50%, -50%); }
  .card--back .wordmark { left: 300px; top: 38px; font-size: 28px; }

  .card__band { position: absolute; inset: 0; width: 100%; height: 100%; }

  .identity {
    position: absolute; right: 318px; top: 196px;
    text-align: right; color: var(--on-band);
  }
  .identity__name { font-size: 10px; letter-spacing: 1px; margin-bottom: 3px; }
  .identity__title { font-size: 8px; color: var(--muted); margin-bottom: 12px; }
  .identity__address { font-size: 8px; line-height: 15px; color: var(--on-band); }

  .divider {
    position: absolute; left: 232px; top: 196px; width: 1px; height: 96px;
    background: var(--muted);
  }
  .contacts {
    position: absolute; left: 244px; top: 200px;
    list-style: none; color: var(--on-band); font-size: 8.5px;
  }
  .contacts__item { display: flex; align-items: center; gap: 7px; height: 18px; white-space: nowrap; }
  .contacts__icon { width: 9px; height: 9px; flex: none; }
</style>
</head>
<body>
<main class="stage">

  <section class="card card--front" aria-label="Business card front">
    <div class="wordmark"><span class="wordmark__dot"></span><span>BrimTrail</span></div>
  </section>

  <section class="card card--back" aria-label="Business card back">
    <svg class="card__band" viewBox="0 0 540 309" aria-hidden="true">
      <path fill="var(--accent)" d="M0,52 C170,34 330,96 420,184 C470,236 510,262 540,266 L540,309 L0,309 Z"/>
      <path fill="var(--card)" d="M0,62 C170,44 330,104 420,192 C470,242 510,268 540,272 L540,309 L0,309 Z"/>
      <path fill="var(--band)" d="M0,68 C170,50 330,110 420,198 C470,248 510,275 540,280 L540,309 L0,309 Z"/>
      <path fill="var(--accent)" d="M400,180 C470,250 510,278 540,283 L540,292 C505,288 465,262 400,190 Z" opacity="0"/>
    </svg>

    <div class="wordmark"><span class="wordmark__dot"></span><span>BrimTrail</span></div>

    <div class="identity">
      <p class="identity__name">Ravindra Kolluparthi</p>
      <p class="identity__title">Vice President</p>
      <p class="identity__address">48260 Hollyfern Market<br>Court, suite 700<br>Ashburn, VA 20147</p>
    </div>

    <div class="divider"></div>

    <ul class="contacts">
      <li class="contacts__item">
        <svg class="contacts__icon" viewBox="0 0 10 10"><circle cx="5" cy="5" r="5" fill="var(--on-band)"/><path d="M3 2.5 L4.3 2.5 L4.8 4 L4 4.6 Q4.8 6 6 6.3 L6.5 5.6 L8 6 L8 7.3 Q4 7.5 3 2.5Z" fill="var(--band)"/></svg>
        <span>571-555-0193</span>
      </li>
      <li class="contacts__item">
        <svg class="contacts__icon" viewBox="0 0 10 10"><circle cx="5" cy="5" r="5" fill="var(--on-band)"/><rect x="3.5" y="2" width="3" height="6" rx=".6" fill="var(--band)"/></svg>
        <span>571-555-0147</span>
      </li>
      <li class="contacts__item">
        <svg class="contacts__icon" viewBox="0 0 10 10"><circle cx="5" cy="5" r="5" fill="var(--on-band)"/><rect x="2.5" y="3.5" width="5" height="3.5" fill="var(--band)"/><rect x="3.5" y="2.2" width="3" height="1.5" fill="var(--band)"/></svg>
        <span>703-555-0162</span>
      </li>
      <li class="contacts__item">
        <svg class="contacts__icon" viewBox="0 0 10 10"><circle cx="5" cy="5" r="5" fill="var(--on-band)"/><rect x="2.4" y="3.2" width="5.2" height="3.6" fill="var(--band)"/><path d="M2.4 3.2 L5 5.2 L7.6 3.2" stroke="var(--on-band)" stroke-width=".6" fill="none"/></svg>
        <span>Ravindra@brimtrailinc.example</span>
      </li>
      <li class="contacts__item">
        <svg class="contacts__icon" viewBox="0 0 10 10"><circle cx="5" cy="5" r="5" fill="var(--on-band)"/><circle cx="5" cy="5" r="2.6" stroke="var(--band)" stroke-width=".8" fill="none"/><path d="M2.4 5 H7.6 M5 2.4 V7.6" stroke="var(--band)" stroke-width=".6"/></svg>
        <span>www.brimtrailinc.example</span>
      </li>
    </ul>
  </section>

</main>
</body>
</html>
```